Website for Cannabis Investment Fund *

We need to create a website for our fund which invests in cannabis projects

Industry/Entity Type

Cannabis

Coding

Coded - Design and coding required

Number of Pages Required

1 page

Colors

Designer to choose only greyscale colors for use in the design.

Requirements
Must have
• Please see the attached file

```html
<!DOCTYPE html>
<html lang="en">
<head>
<meta charset="utf-8">
<title>Verdant Row Capital</title>
<link rel="stylesheet" href="https://fonts.googleapis.com/css2?family=Nunito:wght@400;600&family=Tinos&family=Arimo&display=swap">
<style>
:root{
  --backdrop:#e0ddd7;
  --header:#3b3b3b;
  --nav-text:#ffffff;
  --nav-active:#4cae2e;
  --logo:#8c8c8c;
  --body-text:#555555;
  --card-blue:#0b86d1;
  --card-border:#9cc8e6;
  --node:#7d7d7d;
  --team-bg:#e9ebee;
  --navy:#3b5078;
  --contact-bg:#3d5a8a;
  --white:#ffffff;
}
*{margin:0;padding:0;box-sizing:border-box}
html,body{width:1078px;height:1200px;overflow:hidden;background:var(--backdrop)}
.page{position:absolute;left:316px;top:137px;width:432px;height:981px;background:var(--white);overflow:hidden;font-family:"Nunito",sans-serif}
.abs{position:absolute}
.site-header{left:0;top:0;width:432px;height:25px;background:var(--header);border-bottom:1px solid #888}
.logo{left:17px;top:2px;font-family:"Tinos",serif;font-size:19.5px;color:var(--logo);white-space:nowrap;line-height:20px}
.nav{top:7px;font-size:8.3px;color:var(--nav-text);letter-spacing:.2px;white-space:nowrap}
.nav.active{color:var(--nav-active)}
.hero{left:0;top:25px;width:432px;height:245px;background:radial-gradient(ellipse at 55% 55%,#7fcf8a 0%,#3f9a55 30%,#2c5a37 60%,#1f2a22 100%)}
.hero-caption{left:39px;top:120px;width:360px;height:53px;background:rgba(40,40,40,.72);color:#fff;font-size:12.2px;line-height:14.6px;text-align:center;padding-top:4px;letter-spacing:.2px}
.dot{width:7px;height:7px;border-radius:50%;background:#9a9a9a;top:257px}
.dot.on{background:#fff}
.thesis{left:11px;top:276px;font-size:12.3px;color:var(--body-text);white-space:nowrap;letter-spacing:.2px}
.timeline-line{left:208.5px;top:332px;height:256px;border-left:1px dashed var(--card-blue)}
.node{width:43px;height:43px;border-radius:50%;background:var(--node);color:#fff;font-size:6.6px;display:flex;align-items:center;justify-content:center;text-align:center;line-height:8px}
.card{width:163px;border:1px solid var(--card-border);border-radius:2px;background:#fff;font-family:"Arimo",sans-serif}
.card-title{background:var(--card-blue);color:#fff;font-size:9.6px;line-height:11.6px;padding:2px 5px;height:27px}
.card-body{color:var(--card-blue);font-size:5.3px;line-height:8.5px;padding:4px 5px}
.card.left .card-title,.card.left .card-body{text-align:right}
.card.left::after,.card.right::before{content:"";position:absolute;top:5px;border:4px solid transparent}
.card.left::after{right:-8px;border-left-color:var(--card-blue)}
.card.right::before{left:-8px;border-right-color:var(--card-blue)}
.team{left:0;top:596px;width:432px;height:195px;background:linear-gradient(135deg,#e4e7eb,#eef0f2 50%,#e2e5ea)}
.section-title{width:432px;text-align:center;font-family:"Tinos",serif;font-size:11px;color:#777}
.section-title span{color:var(--navy)}
.sub{width:432px;text-align:center;font-size:4.4px;color:#666}
.filters{width:432px;text-align:center;font-size:4px;color:#777;letter-spacing:.3px;top:668px}
.filters b{color:var(--navy);font-weight:600}
.photo{top:682px;width:82px;height:83px;background:linear-gradient(180deg,#cfcfcf,#8a8a8a 70%,#3e3e3e)}
.contact{left:0;top:791px;width:432px;height:84px;background:radial-gradient(ellipse at 70% 60%,#5b77a6,var(--contact-bg) 55%,#2d4570)}
.contact .section-title{color:#fff}
.contact .sub{color:#dfe5ef}
.btn{top:836px;height:11px;border-radius:6px;font-size:3.6px;letter-spacing:.4px;display:flex;align-items:center;justify-content:center}
.btn.fill{background:#fff;color:#667}
.btn.ghost{border:1px solid #fff;color:#fff}
.icon{width:22px;height:22px;border-radius:50%;background:#fff;box-shadow:0 0 3px rgba(0,0,0,.15);top:928px;display:flex;align-items:center;justify-content:center}
.info-label{font-family:"Tinos",serif;font-size:4px;color:#777;letter-spacing:.3px;top:954px;width:120px;text-align:center}
.info-value{font-size:4.2px;color:var(--navy);top:962px;width:120px;text-align:center}
</style>
</head>
<body>
<div class="page">
  <header class="abs site-header">
    <div class="abs logo">Verdant Row Capital</div>
    <span class="abs nav active" style="left:204px">HOME</span>
    <span class="abs nav" style="left:241px">INVESTMENT FOCUS</span>
    <span class="abs nav" style="left:336px">TEAM</span>
    <span class="abs nav" style="left:371px">CONTACTS</span>
  </header>

  <section class="abs hero" role="img" aria-label="Close-up photograph of a green cannabis plant"></section>
  <div class="abs hero-caption">Thesis: Or goal is to leverage growth of the global cannabis industry by investing in public and private equity of companies in this sector</div>
  <span class="abs dot" style="left:195px"></span>
  <span class="abs dot on" style="left:215px"></span>
  <span class="abs dot" style="left:235px"></span>

  <p class="abs thesis">Thesis: We invest across all steps of the cannabis-product value chain</p>

  <div class="abs timeline-line"></div>
  <div class="abs node" style="left:188px;top:310px">Cultivation</div>
  <div class="abs node" style="left:188px;top:375px">Processing</div>
  <div class="abs node" style="left:189px;top:450px">Value added retail products</div>
  <div class="abs node" style="left:188px;top:516px">Distribution</div>

  <div class="abs card left" style="left:18px;top:334px">
    <div class="card-title">Cultivation facilities – high tech greenhouses</div>
    <div class="card-body">aimed to reduce operational costs and maximize quality of flowers and pre-rolls</div>
  </div>
  <div class="abs card right" style="left:236px;top:398px">
    <div class="card-title">High quality THC and CBD concentrates used</div>
    <div class="card-body">for the enrichment of FMCG or medical end products as well as concentrates available for The direct retail consumption (such as oil and powders) Value</div>
  </div>
  <div class="abs card left" style="left:18px;top:472px">
    <div class="card-title">Value added products in several sectors:</div>
    <div class="card-body">Health and Beauty, Pharmaceutical products, food and beverages</div>
  </div>
  <div class="abs card right" style="left:236px;top:537px">
    <div class="card-title">Promising tools of distribution within the cannabis industry:</div>
    <div class="card-body">e-shops, coffee shop branches etc.</div>
  </div>

  <section class="abs team"></section>
  <h2 class="abs section-title" style="top:620px;font-weight:400">Our <span>Team</span></h2>
  <div class="abs" style="left:207px;top:636px;width:18px;border-top:1px solid var(--navy)"></div>
  <p class="abs sub" style="top:641px">Our team consists of professionals in healthcare and the financial industry</p>
  <p class="abs filters"><b>ALL</b> &nbsp;/&nbsp; INVESTMENT TEAM &nbsp;/&nbsp; ADVISORY BOARD</p>
  <div class="abs photo" style="left:53px" role="img" aria-label="Portrait photo of a team member"></div>
  <div class="abs photo" style="left:135px" role="img" aria-label="Portrait photo of a team member"></div>
  <div class="abs photo" style="left:217px" role="img" aria-label="Portrait photo of a team member"></div>
  <div class="abs photo" style="left:300px" role="img" aria-label="Portrait photo of a team member"></div>

  <section class="abs contact"></section>
  <h2 class="abs section-title" style="top:798px;font-weight:400">Contact Us</h2>
  <p class="abs sub" style="top:812px">If you are an investor interested in learning more about our fund, please send us a message</p>
  <span class="abs btn fill" style="left:175px;width:42px">SEND MESSAGE</span>
  <span class="abs btn ghost" style="left:220px;width:34px">INVESTORS</span>

  <h2 class="abs section-title" style="top:898px;font-weight:400">How to <span>Find Us</span></h2>
  <div class="abs icon" style="left:105px">
    <svg width="8" height="8" viewBox="0 0 8 8"><rect x="2" y=".5" width="4" height="7" rx=".6" fill="none" stroke="#3b5078" stroke-width=".7"/><line x1="3.3" y1="6.5" x2="4.7" y2="6.5" stroke="#3b5078" stroke-width=".6"/></svg>
  </div>
  <div class="abs icon" style="left:204px">
    <svg width="8" height="8" viewBox="0 0 8 8"><path d="M4 1a1.6 1.6 0 0 1 1.6 1.6C5.6 3.8 4 5.5 4 5.5S2.4 3.8 2.4 2.6A1.6 1.6 0 0 1 4 1z" fill="none" stroke="#3b5078" stroke-width=".6"/><path d="M1 4.5h1.5M5.5 4.5H7V7H1V4.5" fill="none" stroke="#3b5078" stroke-width=".6"/></svg>
  </div>
  <div class="abs icon" style="left:304px">
    <svg width="8" height="8" viewBox="0 0 8 8"><rect x=".8" y="1.8" width="6.4" height="4.4" fill="none" stroke="#3b5078" stroke-width=".6"/><path d="M.8 1.8 4 4.4 7.2 1.8" fill="none" stroke="#3b5078" stroke-width=".6"/></svg>
  </div>
  <p class="abs info-label" style="left:56px">PHONE</p>
  <p class="abs info-value" style="left:56px">+41 4100 00000</p>
  <p class="abs info-label" style="left:155px">ADDRESS</p>
  <p class="abs info-value" style="left:155px">Lindenweg 14, 6300 Zug, Switzerland</p>
  <p class="abs info-label" style="left:255px">EMAIL</p>
  <p class="abs info-value" style="left:255px">info@verdantrow.ch</p>
</div>
</body>
</html>
```